Vintage "Greetings from Door County" Design for Wall

I are looking to recreate the vintage "Greetings from" postcard graphic from the 1940-50s. The main focus will be the saying "Greetings from Door County". Door County is a resort area in Wisconsin and we will use this graphic as a backdrop for tourist's instagram pictures. The letters of "Door County" will include things that the area is known for such as swimming, fishing, beaches, boating, biking, camping, cherry orchards, sunsets on the water etc. I have attached an actual postcard from the 50s for Door County to help you visualize the project (Picture 1). I have also attached landmarks and iconic features of Door County to include in the letters (Pictures 2-10). I want it to be more whimsical in nature with drawings to depict these landmarks as opposed to actual realistic pictures (Example 1 & 2). Please ask any questions to help clarify the project. Thanks and good luck!
Target Market(s)
Tourists
Industry/Entity Type
Retail
Colors
Designer to choose colors to be used in the design.
Look and feel

```html
<!DOCTYPE html>
<html lang="en">
<head>
<meta charset="utf-8">
<title>Greetings from Door County</title>
<link rel="stylesheet" href="https://fonts.googleapis.com/css2?family=Titan+One&family=Yellowtail&display=swap">
<style>
  :root {
    --sky-top: #5d8f9c;
    --sky-mid: #7fb1b4;
    --tree-band: #3f6a48;
    --water-top: #5f98a0;
    --water-deep: #2d5678;
    --cream: #ece8d2;
    --cream-dark: #a9a48c;
    --shadow: #141a1c;
  }
  html, body {
    margin: 0;
    padding: 0;
    width: 1200px;
    height: 931px;
    overflow: hidden;
    background: #f2f2f2;
  }
  .postcard {
    display: block;
    width: 1200px;
    height: 931px;
  }
  .big-letter {
    font-family: "Titan One", "Arial Black", sans-serif;
    font-size: 330px;
    text-anchor: middle;
    stroke: var(--cream);
    stroke-width: 9px;
    paint-order: stroke fill;
    stroke-linejoin: round;
  }
  .script {
    font-family: "Yellowtail", cursive;
    stroke: #5a5646;
    stroke-width: 2px;
    paint-order: stroke fill;
  }
  .script-greeting { font-size: 118px; }
  .script-welcome { font-size: 112px; }
</style>
</head>
<body>
<svg class="postcard" viewBox="0 0 1200 931" xmlns="http://www.w3.org/2000/svg">
  <defs>
    <linearGradient id="scene-bg" x1="0" y1="0" x2="0" y2="1">
      <stop offset="0" stop-color="var(--sky-top)"/>
      <stop offset="0.28" stop-color="var(--sky-mid)"/>
      <stop offset="0.42" stop-color="#6f8f78"/>
      <stop offset="0.52" stop-color="var(--tree-band)"/>
      <stop offset="0.6" stop-color="var(--water-top)"/>
      <stop offset="1" stop-color="var(--water-deep)"/>
    </linearGradient>
    <radialGradient id="vignette" cx="0.5" cy="0.5" r="0.75">
      <stop offset="0.55" stop-color="#000" stop-opacity="0"/>
      <stop offset="1" stop-color="#000" stop-opacity="0.45"/>
    </radialGradient>
    <linearGradient id="cream-metal" x1="0" y1="0" x2="0" y2="1">
      <stop offset="0" stop-color="#f4f1e0"/>
      <stop offset="0.55" stop-color="#d9d4ba"/>
      <stop offset="1" stop-color="var(--cream-dark)"/>
    </linearGradient>
    <linearGradient id="fill-autumn-road" x1="0" y1="0" x2="0" y2="1">
      <stop offset="0" stop-color="#d8541c"/><stop offset="0.55" stop-color="#b8431e"/><stop offset="1" stop-color="#3f6d8c"/>
    </linearGradient>
    <linearGradient id="fill-barn" x1="0" y1="0" x2="0" y2="1">
      <stop offset="0" stop-color="#6c6e4a"/><stop offset="0.5" stop-color="#7a3a26"/><stop offset="1" stop-color="#b49d6e"/>
    </linearGradient>
    <linearGradient id="fill-bluff-water" x1="0" y1="0" x2="0" y2="1">
      <stop offset="0" stop-color="#dfe6e4"/><stop offset="0.45" stop-color="#4f7a2c"/><stop offset="1" stop-color="#5c8a94"/>
    </linearGradient>
    <linearGradient id="fill-bluff" x1="0" y1="0" x2="0" y2="1">
      <stop offset="0" stop-color="#5f8a2a"/><stop offset="0.55" stop-color="#c08a3e"/><stop offset="1" stop-color="#9a6b34"/>
    </linearGradient>
    <linearGradient id="fill-ferry" x1="0" y1="0" x2="0" y2="1">
      <stop offset="0" stop-color="#cfd6d8"/><stop offset="0.6" stop-color="#e8ebec"/><stop offset="1" stop-color="#1f2a33"/>
    </linearGradient>
    <linearGradient id="fill-tower" x1="0" y1="0" x2="0" y2="1">
      <stop offset="0" stop-color="#5c93c7"/><stop offset="0.6" stop-color="#6fa2cf"/><stop offset="1" stop-color="#3e7a30"/>
    </linearGradient>
    <linearGradient id="fill-drive-in" x1="0" y1="0" x2="0" y2="1">
      <stop offset="0" stop-color="#3e7a3a"/><stop offset="0.35" stop-color="#d9d3c4"/><stop offset="0.7" stop-color="#2f8a7c"/><stop offset="1" stop-color="#5a7a30"/>
    </linearGradient>
    <linearGradient id="fill-lighthouse" x1="0" y1="0" x2="0" y2="1">
      <stop offset="0" stop-color="#8fb6c2"/><stop offset="0.5" stop-color="#e4e6e2"/><stop offset="1" stop-color="#8a2a22"/>
    </linearGradient>
    <linearGradient id="fill-cherries" x1="0" y1="0" x2="0" y2="1">
      <stop offset="0" stop-color="#3f6a2c"/><stop offset="0.4" stop-color="#c42420"/><stop offset="1" stop-color="#355f2a"/>
    </linearGradient>
    <linearGradient id="fill-fish-boil" x1="0" y1="0" x2="0" y2="1">
      <stop offset="0" stop-color="#c85a1c"/><stop offset="0.5" stop-color="#8a3a1a"/><stop offset="1" stop-color="#f07a1e"/>
    </linearGradient>
    <filter id="block-shadow" x="-20%" y="-20%" width="140%" height="140%">
      <feDropShadow dx="9" dy="9" stdDeviation="2" flood-color="var(--shadow)" flood-opacity="0.9"/>
    </filter>
    <filter id="script-shadow" x="-10%" y="-20%" width="120%" height="150%">
      <feDropShadow dx="4" dy="5" stdDeviation="2" flood-color="var(--shadow)" flood-opacity="0.75"/>
    </filter>
  </defs>

  <g class="backdrop" role="img" aria-label="Lakeside scene at dusk: cloudy teal sky, tree line and calm water reflecting the shore">
    <rect width="1200" height="931" fill="url(#scene-bg)"/>
    <rect width="1200" height="931" fill="url(#vignette)"/>
  </g>

  <text class="script script-greeting" x="31" y="200" fill="url(#cream-metal)" filter="url(#script-shadow)" transform="rotate(-4 31 200)">Greetings from</text>

  <g class="letters" role="img" aria-label="Block letters filled with scenes of the county: autumn road, red barn, limestone bluff, ferry, lookout tower, drive-in theater, lighthouse, cherries and a fish boil">
    <g class="word-door" filter="url(#block-shadow)">
      <text class="big-letter" x="265" y="518" fill="url(#fill-autumn-road)" transform="rotate(-7 265 518)">D</text>
      <text class="big-letter" x="482" y="451" fill="url(#fill-barn)" transform="rotate(-7 482 451)">O</text>
      <text class="big-letter" x="691" y="385" fill="url(#fill-bluff-water)" transform="rotate(-7 691 385)">O</text>
      <text class="big-letter" x="868" y="340" fill="url(#fill-bluff)" transform="rotate(-7 868 340)">R</text>
    </g>
    <g class="word-county" filter="url(#block-shadow)">
      <text class="big-letter" x="1054" y="606" fill="url(#fill-fish-boil)" transform="rotate(-7 1054 606)">Y</text>
      <text class="big-letter" x="872" y="619" fill="url(#fill-cherries)" transform="rotate(-7 872 619)">T</text>
      <text class="big-letter" x="696" y="674" fill="url(#fill-lighthouse)" transform="rotate(-7 696 674)">N</text>
      <text class="big-letter" x="505" y="719" fill="url(#fill-drive-in)" transform="rotate(-7 505 719)">U</text>
      <text class="big-letter" x="313" y="761" fill="url(#fill-tower)" transform="rotate(-7 313 761)">O</text>
      <text class="big-letter" x="138" y="792" fill="url(#fill-ferry)" transform="rotate(-7 138 792)">C</text>
    </g>
  </g>

  <text class="script script-welcome" x="694" y="700" fill="url(#cream-metal)" filter="url(#script-shadow)" transform="rotate(-5 694 700)">Welcome!</text>
</svg>
</body>
</html>
```